CONTACT US Page and design for website

We need a contact us page for our website. We would like it to have a message area, a map, our information, etc.

Please see the text attachment for what we are looking for. We need to have something that is creative and interesting, modern and professional.

We believe that a contact US page should be very creative because everyone clicks that to contact us. We want it to be super professional, attention grabbing, pleasing to the eye.

PLEASE KEEP THE HEADER AND FOOTER THE SAME, ONLY THE ACTUAL CONTACT US PAGE NEEDS TO BE WORKED ON. THANKS!
We are excited to work with designers for this project.

Target Market(s)

Clients in technology business

Industry/Entity Type

Information Technology

Number of Pages Required

1 page

Font styles to use
Serif

Requirements
Must have
• CHECK THE TEXT ATTACHMENT PLEASE
• Must stay within our design colors and theme.
Nice to have
• see attachment
Should not have
• it should be special

```html
<!DOCTYPE html>
<html lang="en">
<head>
<meta charset="utf-8">
<title>Contact Us – Nexora Tech</title>
<link rel="stylesheet" href="https://fonts.googleapis.com/css2?family=Montserrat:wght@400;500;600&family=Arimo:wght@400;700&display=swap">
<style>
:root{
  --teal:#33bab0;
  --teal-dark:#27a79d;
  --ink:#2f2f2f;
  --muted:#8a8a8a;
  --line:#dcdcdc;
  --soft:#f3f3f3;
  --footer:#a3a3a3;
  --footer-dark:#939393;
  --white:#ffffff;
}
*{box-sizing:border-box;margin:0;padding:0}
html,body{width:1200px;height:3120px;overflow:hidden;background:var(--white)}
body{position:relative;font-family:"Montserrat",sans-serif;color:var(--ink)}
.abs{position:absolute}
svg{display:block}

/* header */
.site-header{left:0;top:0;width:1200px;height:150px;border-bottom:1px solid var(--line)}
.brand{left:87px;top:22px;display:flex;align-items:center;gap:16px}
.brand-dot{width:62px;height:62px;border-radius:50%;background:var(--teal)}
.brand-name{font-size:40px;font-weight:600;color:var(--teal);letter-spacing:1px}
.account-tab{left:930px;top:0;width:158px;height:30px;background:#7a7a7a;border-radius:0 0 0 12px;display:flex;justify-content:space-around;align-items:center;font-size:11px;color:#eee;letter-spacing:1px}
.contact-quick{left:812px;top:48px;display:flex;align-items:center;gap:10px;font-size:14px;color:#777}
.icon-circle{width:38px;height:38px;border-radius:50%;border:2px solid var(--teal);display:flex;align-items:center;justify-content:center}
.header-phone{font-size:21px;color:var(--ink);margin-left:4px}
.header-rule{left:0;top:100px;width:1200px;height:1px;background:var(--line)}
.main-nav{left:85px;top:117px;display:flex;gap:22px;font-size:11px;letter-spacing:.5px;color:#444}
.search-box{left:890px;top:108px;width:173px;height:35px;border:1.5px solid #bbb;border-radius:18px;display:flex;align-items:center;justify-content:space-between;padding:0 12px 0 20px;font-size:11px;color:#555}
.cart-btn{left:1076px;top:106px;width:38px;height:38px;border-radius:50%;border:1.5px solid #bbb;display:flex;align-items:center;justify-content:center}
.breadcrumb{left:0;top:150px;width:1200px;height:37px;background:var(--teal);color:var(--white);font-size:12px;padding:10px 0 0 85px}

/* contact form */
.help-icon{left:573px;top:262px}
.help-title{left:0;top:312px;width:1200px;text-align:center;font-size:32px;font-weight:400;letter-spacing:3px;color:#333}
.help-intro{left:300px;top:364px;width:600px;text-align:center;font-size:13px;line-height:24px;letter-spacing:1px;color:#333}
.contact-form{left:308px;top:484px;width:584px}
.field{position:relative;height:64px;border-bottom:1.5px solid var(--line);display:flex;align-items:center;justify-content:space-between;font-size:13px;letter-spacing:1.5px;color:var(--muted)}
.field.filled{color:var(--ink)}
.submit-btn{margin-top:52px;height:50px;background:var(--teal);color:var(--white);display:flex;align-items:center;justify-content:center;font-size:14px;font-weight:500;letter-spacing:1.5px}
.section-rule{left:280px;top:886px;width:640px;height:1px;background:linear-gradient(90deg,transparent,#e0e0e0,transparent)}

/* headquarters */
.hq-title{left:0;top:958px;width:1200px;text-align:center;font-size:22px;font-weight:500;letter-spacing:1.5px;color:var(--teal)}
.hq-address{left:0;top:998px;width:1200px;text-align:center;font-size:17px;line-height:26px;letter-spacing:2px;color:#333}
.hq-mark{left:550px;top:1124px;width:100px;height:100px;border-radius:50%;background:var(--teal)}

/* map */
.map-area{left:0;top:1279px;width:1200px;height:437px;border-top:2px solid var(--teal);border-bottom:2px solid var(--teal);background:linear-gradient(135deg,#ebebe6,#f2efe6 45%,#e6e9e8)}

/* hours */
.hours{left:0;top:1716px;width:1200px;height:193px;background:var(--soft);border-bottom:1px solid var(--line)}
.hours-head{left:84px;top:56px;display:flex;gap:14px;align-items:flex-start}
.hours-title{font-size:16px;font-weight:500;line-height:22px;letter-spacing:1px;margin-top:2px}
.hours-list{list-style:none;font-size:14px;letter-spacing:1px}
.hours-list li{position:absolute;white-space:nowrap}
.hours-list li::before{content:"";position:absolute;left:-24px;top:6px;width:7px;height:7px;border-radius:50%;background:var(--teal)}
.service-note{left:0;top:1909px;width:1200px;height:107px;background:var(--soft);text-align:center;padding-top:42px;font-size:17px;font-weight:500;letter-spacing:1.5px}

/* social band */
.stay-band{left:0;top:2016px;width:1200px;height:160px;background:var(--teal);color:var(--white)}
.stay-label{left:84px;top:64px;display:flex;align-items:center;gap:12px;font-size:18px;font-weight:600;letter-spacing:1px}
.social-dots{left:890px;top:64px;display:flex;gap:38px}
.social-dots span{width:26px;height:26px;border-radius:50%;border:2.5px solid var(--white)}

/* inquiries */
.inquiries{left:0;top:2176px;width:1200px;height:482px;background:linear-gradient(180deg,#ececec,#e1e1e1)}
.desk-photo{left:666px;top:0;width:534px;height:482px;background:linear-gradient(160deg,#e6e6e6 0%,#d0d0d0 55%,#f0eeee 100%)}
.inquiry{left:86px;display:flex;gap:14px}
.inquiry h3{font-size:18px;font-weight:500;letter-spacing:1px;color:#333;margin-bottom:8px}
.inquiry p{font-size:14px;letter-spacing:1.5px;line-height:21px;color:#333}

/* footer */
.site-footer{left:0;top:2658px;width:1200px;height:462px;background:var(--footer);color:var(--white);font-family:"Arimo",sans-serif}
.footer-about{left:200px;top:20px;width:800px;text-align:center;font-size:14.5px;line-height:21px}
.footer-contacts{top:118px;font-size:15px;display:flex;gap:10px;align-items:flex-start;line-height:21px}
.footer-links{top:196px;font-size:16.5px}
.footer-support{left:830px;top:196px;font-size:16.5px}
.footer-support ul{list-style:none;font-size:10px;font-weight:700;line-height:12px;margin:6px 0 0 16px}
.footer-social{left:0;top:285px;width:1200px;height:77px;background:var(--footer-dark);display:flex;justify-content:center;align-items:center;gap:18px}
.footer-social span{width:36px;height:36px;border-radius:50%;border:1.5px solid #d8d8d8}
.footer-base{left:0;top:362px;width:1200px;height:100px;border-top:1px solid #c4c4c4;display:flex;justify-content:center;align-items:center;gap:10px;font-size:12px;line-height:16px}
.footer-base .square{width:22px;height:22px;background:#dcdcdc}
</style>
</head>
<body>

<header class="site-header abs">
  <div class="brand abs"><span class="brand-dot"></span><span class="brand-name">NEXORA TECH</span></div>
  <div class="account-tab abs"><span>SIGN UP</span><span>LOGIN</span></div>
  <div class="contact-quick abs">
    <span class="icon-circle"><svg width="18" height="16" viewBox="0 0 18 16"><path d="M2 2h14v9H7l-4 3v-3H2z" fill="var(--teal)"/></svg></span>
    <span>LIVE CHAT</span>
    <span class="icon-circle" style="margin-left:34px"><svg width="16" height="16" viewBox="0 0 24 24"><path d="M6.6 10.8a15 15 0 0 0 6.6 6.6l2.2-2.2a1 1 0 0 1 1-.25 11 11 0 0 0 3.6.6 1 1 0 0 1 1 1V20a1 1 0 0 1-1 1A17 17 0 0 1 3 4a1 1 0 0 1 1-1h3.5a1 1 0 0 1 1 1 11 11 0 0 0 .6 3.6 1 1 0 0 1-.25 1z" fill="var(--teal)"/></svg></span>
    <span class="header-phone">555-014-2290</span>
  </div>
  <div class="header-rule abs"></div>
  <nav class="main-nav abs">
    <span>SERVERS</span><span>WORKSTATIONS</span><span>COMPONENTS</span><span>VIRTUAL REALITY</span><span>DRONES</span><span>ABOUT US</span><span>BLOG</span><span>RESOURCES</span><span>CONTACT US</span>
  </nav>
  <div class="search-box abs"><span>Search</span><svg width="14" height="14" viewBox="0 0 14 14"><circle cx="6" cy="6" r="4.5" fill="none" stroke="var(--teal)" stroke-width="2"/><path d="M9.5 9.5l3.5 3.5" stroke="var(--teal)" stroke-width="2"/></svg></div>
  <div class="cart-btn abs"><svg width="18" height="16" viewBox="0 0 18 16"><path d="M1 2h3l2 9h9l2-7H5" fill="none" stroke="var(--teal)" stroke-width="2"/><circle cx="7" cy="14" r="1.4" fill="var(--teal)"/><circle cx="14" cy="14" r="1.4" fill="var(--teal)"/></svg></div>
</header>
<div class="breadcrumb abs">HOME / CONTACT US</div>

<main>
  <svg class="help-icon abs" width="54" height="38" viewBox="0 0 54 38"><rect x="2" y="2" width="50" height="34" fill="none" stroke="var(--teal)" stroke-width="2.5"/><path d="M2 2l25 20 25-20M2 36l19-17M52 36L33 19" fill="none" stroke="var(--teal)" stroke-width="2.5"/></svg>
  <h1 class="help-title abs">HOW CAN WE HELP?</h1>
  <p class="help-intro abs">Please get in contact with us today regarding your Enterprise IT Hardware service and equipments information or to discuss your appointment.</p>

  <form class="contact-form abs">
    <div class="field"><span>Name</span><svg width="22" height="22" viewBox="0 0 22 22"><circle cx="11" cy="11" r="10" fill="none" stroke="#999" stroke-width="1.4"/><circle cx="11" cy="8.5" r="3.5" fill="none" stroke="#999" stroke-width="1.4"/><path d="M4.5 17.5c2-3.5 11-3.5 13 0" fill="none" stroke="#999" stroke-width="1.4"/></svg></div>
    <div class="field filled"><span>Sample@testemail.com</span><svg width="24" height="24" viewBox="0 0 24 24"><circle cx="12" cy="12" r="11" fill="none" stroke="var(--teal)" stroke-width="1.6"/><path d="M7 12.5l3.4 3.4L17 9" fill="none" stroke="var(--teal)" stroke-width="1.8"/></svg></div>
    <div class="field"><span>Phone number</span><svg width="16" height="24" viewBox="0 0 16 24"><rect x="1" y="1" width="14" height="22" rx="2" fill="none" stroke="#999" stroke-width="1.4"/><path d="M1 5h14M1 18h14" stroke="#999" stroke-width="1.4"/></svg></div>
    <div class="field"><span>Message</span><svg width="22" height="20" viewBox="0 0 22 20"><path d="M1 1h20v13H8l-4 4v-4H1z" fill="none" stroke="#999" stroke-width="1.4"/></svg></div>
    <div class="submit-btn">Submit</div>
  </form>
  <div class="section-rule abs"></div>

  <h2 class="hq-title abs">OFFICE HEADQUARTERS</h2>
  <address class="hq-address abs" style="font-style:normal">Nexora Tech, LLC.<br>4820 Larkspur Ave.<br>Westbrook, CA 90417</address>
  <div class="hq-mark abs"></div>

  <div class="map-area abs" role="img" aria-label="Street map showing the office location"></div>

  <section class="hours abs">
    <div class="hours-head abs">
      <svg width="34" height="34" viewBox="0 0 34 34"><circle cx="17" cy="17" r="15" fill="none" stroke="var(--teal)" stroke-width="2"/><path d="M17 8v10h7" fill="none" stroke="var(--teal)" stroke-width="2"/></svg>
      <div class="hours-title">HOURS OF<br>OPERATION</div>
    </div>
    <ul class="hours-list">
      <li style="left:428px;top:53px">Monday: 8:00am- 5:00pm</li>
      <li style="left:833px;top:53px">Tuesday:8:00am- 5:00pm</li>
      <li style="left:428px;top:86px">Wednesday: 8:00am- 5:00pm</li>
      <li style="left:833px;top:86px">Thursday: 8:00am- 5:00pm</li>
      <li style="left:428px;top:118px">Friday: 8:00am- 5:00pm</li>
    </ul>
  </section>
  <p class="service-note abs">Our dedicated customer service representatives are available 24/7 by phone.</p>

  <section class="stay-band abs">
    <div class="stay-label abs">
      <svg width="36" height="32" viewBox="0 0 36 32"><circle cx="6" cy="16" r="4.5" fill="none" stroke="#fff" stroke-width="2"/><circle cx="28" cy="6" r="4.5" fill="none" stroke="#fff" stroke-width="2"/><circle cx="28" cy="26" r="4.5" fill="none" stroke="#fff" stroke-width="2"/><path d="M10 14l14-6M10 18l14 6" stroke="#fff" stroke-width="2"/></svg>
      STAY CONNECTED:
    </div>
    <div class="social-dots abs"><span></span><span></span><span></span><span></span></div>
  </section>

  <section class="inquiries abs">
    <div class="desk-photo abs" role="img" aria-label="Desk with a laptop, a smartphone, sticky notes and pens"></div>
    <div class="inquiry abs" style="top:76px">
      <svg width="24" height="24" viewBox="0 0 24 24"><path d="M6.6 10.8a15 15 0 0 0 6.6 6.6l2.2-2.2a1 1 0 0 1 1-.25 11 11 0 0 0 3.6.6 1 1 0 0 1 1 1V20a1 1 0 0 1-1 1A17 17 0 0 1 3 4a1 1 0 0 1 1-1h3.5a1 1 0 0 1 1 1 11 11 0 0 0 .6 3.6 1 1 0 0 1-.25 1z" fill="var(--teal)"/></svg>
      <div><h3>GENERAL INQUIRIES</h3><p>(555)014-2290<br>info@nexoratech.com</p></div>
    </div>
    <div class="inquiry abs" style="top:202px">
      <svg width="24" height="24" viewBox="0 0 24 24"><path d="M6.6 10.8a15 15 0 0 0 6.6 6.6l2.2-2.2a1 1 0 0 1 1-.25 11 11 0 0 0 3.6.6 1 1 0 0 1 1 1V20a1 1 0 0 1-1 1A17 17 0 0 1 3 4a1 1 0 0 1 1-1h3.5a1 1 0 0 1 1 1 11 11 0 0 0 .6 3.6 1 1 0 0 1-.25 1z" fill="var(--teal)"/></svg>
      <div><h3>SALES INQUIRIES</h3><p>(555)014-2290<br>sales@nexoratech.com</p></div>
    </div>
    <div class="inquiry abs" style="top:327px">
      <svg width="24" height="24" viewBox="0 0 24 24"><path d="M6.6 10.8a15 15 0 0 0 6.6 6.6l2.2-2.2a1 1 0 0 1 1-.25 11 11 0 0 0 3.6.6 1 1 0 0 1 1 1V20a1 1 0 0 1-1 1A17 17 0 0 1 3 4a1 1 0 0 1 1-1h3.5a1 1 0 0 1 1 1 11 11 0 0 0 .6 3.6 1 1 0 0 1-.25 1z" fill="var(--teal)"/></svg>
      <div><h3>PURCHASING INQUIRIES</h3><p>(555)014-2291<br>purchasing@nexoratech.com</p></div>
    </div>
  </section>
</main>

<footer class="site-footer abs">
  <p class="footer-about abs">Based in Westbrook California, Nexora Tech offers custom servers, storage, and workstations for local businesses in Los Angeles, Beverly Hills, Thousand Oaks, Ventura, Orange County, Santa Barbara, Oxnard, Irvine, Anaheim, and San Diego. Nexora Tech also offers such products to clients throughout the United States and Worldwide.</p>
  <div class="footer-contacts abs" style="left:258px"><svg width="12" height="16" viewBox="0 0 12 16"><path d="M6 0a6 6 0 0 0-6 6c0 4.5 6 10 6 10s6-5.5 6-10a6 6 0 0 0-6-6zm0 8.5A2.5 2.5 0 1 1 6 3.5a2.5 2.5 0 0 1 0 5z" fill="#fff"/></svg><span>4820 Larkspur Ave<br>Westbrook, CA 90417</span></div>
  <div class="footer-contacts abs" style="left:520px"><svg width="14" height="14" viewBox="0 0 24 24"><path d="M6.6 10.8a15 15 0 0 0 6.6 6.6l2.2-2.2a1 1 0 0 1 1-.25 11 11 0 0 0 3.6.6 1 1 0 0 1 1 1V20a1 1 0 0 1-1 1A17 17 0 0 1 3 4a1 1 0 0 1 1-1h3.5a1 1 0 0 1 1 1 11 11 0 0 0 .6 3.6 1 1 0 0 1-.25 1z" fill="#fff"/></svg><span>555-014-2290</span></div>
  <div class="footer-contacts abs" style="left:746px"><svg width="16" height="12" viewBox="0 0 16 12"><rect width="16" height="12" rx="1" fill="#fff"/><path d="M0 1l8 6 8-6" fill="none" stroke="var(--footer)" stroke-width="1.4"/></svg><span>sales@nexoratech.com</span></div>
  <span class="footer-links abs" style="left:171px">Computer Hardware</span>
  <span class="footer-links abs" style="left:396px">Drones</span>
  <span class="footer-links abs" style="left:506px">Virtual Reality</span>
  <span class="footer-links abs" style="left:674px">About Us</span>
  <div class="footer-support abs">Customer Support
    <ul><li>Terms and Conditions</li><li>Warranty Information</li><li>Contact Us</li><li>Return Policy</li></ul>
  </div>
  <div class="footer-social abs"><span></span><span></span><span></span><span></span></div>
  <div class="footer-base abs"><span class="square"></span><span>Nexora Tech, LLC.<br>Copyright © 2017</span></div>
</footer>

</body>
</html>
```